VelmiTaro 16 pages booklet CD Cover

I need a cover (also formatted to be used for digital release), a 16 Pages Booklet + Inlay both sides, a back cover, and a CD image for french pop-rock album.

The name of the artist : Velmitaro
The name of the album : Marcher sous la brume (which means "walking under the mist")
Style of music: I've attached some mp3 extracts. In a few words, this is electro POP music, I'm inspired by band such as The Haze, etc..

This album talks about the desire to live elsewhere, in a world more just and equitable, less painful. The songs talk about people fighting to find a job, to feed their son, poeple who would like to have enough money to enjoy life, etc... but as they can't, at least, they dream about a new world, they draw this elsewhere, hence the title of the album "Marcher sous la brume"

Font styles to use
Sans Serif

Colors
b768aa
33a6d7

Requirements
Must have
• COver: fell free to make your porposal as long as it match the project description objectoves.
• I have add/attached a document "CD Cover Structure" that explains the stucture of the cover, and how i think it could be setup. BUt any other proposal will be welcome.
• For the last one, we will put the song titles and i will let you make me some suggestions.
Nice to have
• the songs are rather melancholy (but not sad) and it would be nice to transmit this impression by the colors. That's why i have chose the pink and blue as primary colours.

```html
<!DOCTYPE html>
<html lang="fr">
<head>
<meta charset="utf-8">
<title>VELMITARO – Marcher sous la brume</title>
<link rel="stylesheet" href="https://fonts.googleapis.com/css2?family=Amatic+SC:wght@400;700&family=Dancing+Script:wght@400;500&display=swap">
<style>
  :root {
    --paper: #e9e4dc;
    --paper-shade: #ddd6cb;
    --ink-navy: #2a4668;
    --sea-teal: #3bbfa8;
    --sea-deep: #1f8f86;
    --sea-mint: #8fe0c8;
    --sky-blue: #5fb6d6;
  }
  * { margin: 0; padding: 0; box-sizing: border-box; }
  html, body {
    width: 1200px;
    height: 1200px;
    overflow: hidden;
    background: var(--paper);
  }
  .cover {
    position: relative;
    width: 1200px;
    height: 1200px;
    overflow: hidden;
    background:
      radial-gradient(circle at 20% 80%, var(--paper-shade) 0%, transparent 45%),
      radial-gradient(circle at 85% 15%, #efebe4 0%, transparent 40%),
      var(--paper);
  }
  .globe-artwork {
    position: absolute;
    left: 0;
    top: 120px;
    width: 1200px;
    height: 960px;
  }
  .artist-name {
    position: absolute;
    top: 62px;
    right: 180px;
    font-family: "Amatic SC", cursive;
    font-weight: 700;
    font-size: 66px;
    letter-spacing: 4px;
    color: var(--ink-navy);
  }
  .album-title {
    position: absolute;
    left: 607px;
    top: 571px;
    transform: translate(-50%, -50%);
    text-align: center;
    color: var(--ink-navy);
    line-height: 1;
  }
  .album-title .script-line {
    display: block;
    font-family: "Dancing Script", cursive;
    font-weight: 400;
    font-size: 120px;
  }
  .album-title .caps-line {
    display: block;
    font-family: "Amatic SC", cursive;
    font-weight: 400;
    font-size: 78px;
    letter-spacing: 4px;
    margin: 6px 0 2px;
  }
</style>
</head>
<body>
  <main class="cover">
    <svg class="globe-artwork" viewBox="0 0 1200 960" role="img" aria-label="Watercolour illustration of a teal and mint globe surrounded by loose paint splashes">
      <defs>
        <radialGradient id="splash-wash" cx="50%" cy="47%" r="50%">
          <stop offset="0%" stop-color="var(--sea-teal)" stop-opacity="0.55"/>
          <stop offset="55%" stop-color="var(--sea-deep)" stop-opacity="0.45"/>
          <stop offset="80%" stop-color="var(--sky-blue)" stop-opacity="0.2"/>
          <stop offset="100%" stop-color="var(--sky-blue)" stop-opacity="0"/>
        </radialGradient>
        <radialGradient id="globe-wash" cx="45%" cy="40%" r="60%">
          <stop offset="0%" stop-color="var(--paper)"/>
          <stop offset="55%" stop-color="#cfe9dd"/>
          <stop offset="100%" stop-color="var(--sea-mint)"/>
        </radialGradient>
      </defs>
      <ellipse class="paint-splash" cx="600" cy="450" rx="600" ry="470" fill="url(#splash-wash)"/>
      <circle class="globe" cx="607" cy="451" r="348" fill="url(#globe-wash)"/>
    </svg>

    <div class="artist-name">VELMITARO</div>

    <h1 class="album-title">
      <span class="script-line">marcher</span>
      <span class="caps-line">SOUS LA</span>
      <span class="script-line">brume</span>
    </h1>
  </main>
</body>
</html>
```